Conference program advertisement

Our business www.clinic ledgerwise.com.au is a good sponsor of the conference program run by the Pacific Rim Guild of Perioperative Medicine (PRGPM) here in Western Australia.
We have been running the same ad for a while and so we could do with a fresh new presence.
We have a conference banner and other signage that we'll use at the trade show so we're not looking to rebrand. Just looking for a new ad.
Specification is full colour A4, high res PDF
(Because I'm using my phone to create this job, I cannot seem to upload the existing ad. I'll do do ASAP.)

Target Market(s)

Specialist doctors

Industry/Entity Type

Trade

Font styles to use
Sans Serif

Colors

Designer to choose colors to be used in the design.

Requirements
Must have
• A4
Existing logo and colour scheme

```html
<!DOCTYPE html>
<html lang="en">
<head>
<meta charset="utf-8">
<title>Clinic Ledgerwise Services – Conference Advertisement</title>
<link href="https://fonts.googleapis.com/css2?family=Roboto+Condensed:wght@300;700&family=Arimo:ital,wght@0,400;0,700;1,400;1,700&display=swap" rel="stylesheet">
<style>
  :root {
    --page: #ffffff;
    --frame: #f1dfe3;
    --navy: #0c3f78;
    --navy-deep: #08305e;
    --royal: #1d5ea6;
    --cyan: #4fc6ec;
    --ink: #0d4a86;
    --black: #000000;
    --white: #ffffff;
  }
  * { margin: 0; padding: 0; box-sizing: border-box; }
  html, body { width: 900px; height: 1200px; overflow: hidden; background: var(--page); }
  .canvas { position: relative; width: 900px; height: 1200px; background: var(--page); }
  .frame { position: absolute; left: 90px; top: 90px; width: 724px; height: 1023px; border: 1px solid var(--frame); background: #fdfbfb; }
  .ad { position: absolute; left: 107px; top: 107px; width: 690px; height: 988px; background: var(--white); overflow: hidden; }
  .ad-shapes { position: absolute; left: 0; top: 0; width: 690px; height: 988px; }

  .headline { position: absolute; left: 30px; top: 34px; color: var(--ink); font-family: "Roboto Condensed", "Arial Narrow", sans-serif; text-transform: uppercase; line-height: 1; }
  .headline-lead { display: block; font-weight: 300; font-size: 41px; letter-spacing: -0.5px; }
  .headline-main { display: block; font-weight: 700; font-size: 74px; letter-spacing: -1.5px; margin-top: 0; }
  .headline-tail { display: block; font-weight: 700; font-size: 33px; margin-top: 0; }

  .brand { position: absolute; left: 383px; top: 540px; display: flex; align-items: center; gap: 10px; }
  .brand-mark { width: 14px; height: 14px; background: var(--ink); }
  .brand-name { font-family: Arimo, Arial, sans-serif; font-weight: 700; font-size: 18px; line-height: 20px; color: var(--ink); }

  .copy { position: absolute; left: 383px; top: 615px; width: 290px; font-family: Arimo, Arial, sans-serif; font-size: 13.2px; line-height: 16px; color: var(--ink); }
  .copy p { text-align: justify; }
  .copy .cta { margin-top: 16px; font-weight: 700; font-style: italic; }
  .copy .contact { margin-top: 16px; font-style: italic; }
  .copy .contact strong { font-weight: 700; }

  .office { position: absolute; left: 13px; top: 852px; width: 175px; font-family: Arimo, Arial, sans-serif; font-size: 11px; line-height: 15px; color: var(--white); font-style: italic; }
  .office h3 { font-style: normal; font-weight: 700; font-size: 11px; text-transform: uppercase; }
  .office .postal { margin-top: 18px; }

  .services { position: absolute; top: 890px; list-style: none; font-family: Arimo, Arial, sans-serif; font-size: 10.6px; line-height: 13.2px; color: var(--ink); text-transform: uppercase; }
  .services li::before { content: "• "; }
  .services-a { left: 232px; }
  .services-b { left: 383px; }
</style>
</head>
<body>
<div class="canvas">
  <div class="frame"></div>
  <div class="ad">
    <svg class="ad-shapes" viewBox="0 0 690 988" xmlns="http://www.w3.org/2000/svg">
      <defs>
        <linearGradient id="photoTone" x1="0" y1="0" x2="1" y2="1">
          <stop offset="0" stop-color="#e9f3f8"/>
          <stop offset="0.5" stop-color="#b9e3e0"/>
          <stop offset="1" stop-color="#dfeaf1"/>
        </linearGradient>
        <linearGradient id="bandTone" x1="0" y1="0" x2="1" y2="0">
          <stop offset="0" stop-color="#0e4a8c"/>
          <stop offset="1" stop-color="#08305e"/>
        </linearGradient>
        <linearGradient id="stripeTone" x1="0" y1="0" x2="0.4" y2="1">
          <stop offset="0" stop-color="#2f74b8"/>
          <stop offset="1" stop-color="#ffffff"/>
        </linearGradient>
        <linearGradient id="lineTone" x1="0" y1="0" x2="0" y2="1">
          <stop offset="0" stop-color="#2c6aa6"/>
          <stop offset="1" stop-color="#e2edf6"/>
        </linearGradient>
      </defs>
      <polygon class="photo" role="img" aria-label="Photograph of a smiling doctor in green scrubs with a stethoscope holding a blue folder in a bright clinic" points="0,0 690,0 690,290 120,425 0,165" fill="url(#photoTone)"/>
      <polygon class="accent-cyan" points="0,163 121,423 51,565 0,470" fill="var(--cyan)"/>
      <polygon class="band" points="121,423 690,286 690,405 51,565" fill="url(#bandTone)"/>
      <polygon class="stripe" points="53,567 178,535 375,988 220,988" fill="url(#stripeTone)"/>
      <polygon class="stripe-line" points="183,533 190,531 384,988 377,988" fill="url(#lineTone)"/>
      <polygon class="corner" points="0,628 46,583 218,988 0,988" fill="var(--black)"/>
    </svg>

    <h1 class="headline">
      <span class="headline-lead">Is administration</span>
      <span class="headline-main">Eating up</span>
      <span class="headline-tail">Your valuable time?</span>
    </h1>

    <div class="brand">
      <div class="brand-mark"></div>
      <div class="brand-name">Clinic Ledgerwise Services</div>
    </div>

    <div class="copy">
      <p>Admin can consume a large amount of time for doctors working in private practice.<br>From generating accounts to chasing up bad debts, from sitting on hold with health funds, or trawling through remittance advices to getting accreditation papers and submitting provider number applications properly – we’re sure you would prefer to focus on being a doctor rather than worrying about paperwork and piles of admin.</p>
      <p class="cta">Clinic Ledgerwise Services is here to help.</p>
      <p class="contact"><strong>contact us today</strong><br>if you’re ready to remove the burden of admin.</p>
    </div>

    <address class="office">
      <h3>Office address</h3>
      <p>Level 2, Suite 18, 415<br>Harbour Road, East Perth,<br>WA, 6004</p>
      <p class="postal">PO Box 377, East Perth WA 6892<br>mia@clinicledgerwise.com.au<br>www.clinic ledgerwise.com.au</p>
    </address>

    <ul class="services services-a">
      <li>Private billing</li>
      <li>VMP billing</li>
      <li>Practice management</li>
      <li>Organise lists</li>
      <li>Cover lists</li>
      <li>Banking</li>
    </ul>
    <ul class="services services-b">
      <li>Medicare and health fund registrations</li>
      <li>Fee estimates and informed financial consent</li>
      <li>Direct bill and credit card payments</li>
      <li>Electronic claiming to health funds</li>
      <li>GST reporting</li>
      <li>Hospital accreditations</li>
    </ul>
  </div>
</div>
</body>
</html>
```